Banner Ad Design Project

We are a training organization and require a banner which we can use to promate our brand and our services at trade shows, you may visit our website: www.harlowinstitute.net.au to obtain ideas

Its a trade show banner which pull out with a stand

Size: ( 750 X 2000 mm )

we have a logo which you may have .

Industry/Entity Type

Training

```html
<!DOCTYPE html>
<html lang="en">
<head>
<meta charset="UTF-8">
<title>Harlow Institute – Trade Show Banner</title>
<link href="https://fonts.googleapis.com/css2?family=Source+Sans+3:wght@400;600;700&display=swap" rel="stylesheet">
<style>
  :root {
    --brand-blue: #29a8e0;
    --white: #ffffff;
    --photo-warm: #c9a15a;
    --photo-mid: #b8b2a8;
    --photo-dark: #5e4634;
  }
  html, body {
    margin: 0;
    padding: 0;
    width: 1200px;
    height: 4743px;
    overflow: hidden;
    background: var(--white);
  }
  .banner {
    position: relative;
    width: 1200px;
    height: 4743px;
    background: var(--brand-blue);
    color: var(--white);
    font-family: "Source Sans 3", "Myriad Pro", sans-serif;
    overflow: hidden;
  }
  .award-strip {
    position: absolute;
    left: 0; top: 14px;
    width: 1200px;
    height: 90px;
    border-top: 10px solid var(--white);
    border-bottom: 10px solid var(--white);
    box-sizing: border-box;
    display: flex;
    align-items: center;
    padding-left: 40px;
    font-size: 46px;
    letter-spacing: 0.5px;
  }
  .brand {
    position: absolute;
    left: 44px; top: 180px;
    display: flex;
    align-items: center;
    gap: 30px;
    font-size: 104px;
    font-weight: 400;
    line-height: 1;
  }
  .brand-mark {
    width: 70px;
    height: 70px;
    background: var(--white);
  }
  .centered {
    position: absolute;
    left: 0;
    width: 1200px;
    text-align: center;
    line-height: 1;
  }
  .headline { top: 700px; font-size: 150px; font-weight: 400; }
  .subhead { top: 865px; font-size: 100px; font-weight: 400; }
  .question { top: 1405px; font-size: 72px; font-weight: 700; }
  .tagline { top: 1500px; font-size: 54px; font-weight: 400; }
  .photo {
    position: absolute;
    left: 0; top: 1700px;
    width: 1200px;
    height: 2095px;
    background: linear-gradient(100deg, var(--photo-warm) 0%, #d9c9a6 30%, var(--photo-mid) 55%, #8f7a66 80%, var(--photo-dark) 100%);
  }
  .cta { top: 3850px; font-size: 88px; font-weight: 700; }
  .enquire { top: 4195px; font-size: 76px; font-weight: 400; }
  .phone { top: 4320px; font-size: 76px; font-weight: 700; }
  .email { top: 4435px; font-size: 50px; font-weight: 400; }
  .web-strip {
    position: absolute;
    left: 0; top: 4600px;
    width: 1200px;
    height: 80px;
    background: var(--white);
    color: var(--brand-blue);
    text-align: center;
    font-size: 54px;
    line-height: 80px;
  }
</style>
</head>
<body>
<main class="banner">
  <div class="award-strip">Awarded the best public sector development in the world</div>

  <div class="brand">
    <span class="brand-mark"></span>
    <span class="brand-name">Harlow Institute</span>
  </div>

  <h1 class="centered headline" style="margin:0">A Bright Future</h1>
  <p class="centered subhead" style="margin:0">We get you ready</p>

  <h2 class="centered question" style="margin:0">Why choose Harlow Institute?</h2>
  <p class="centered tagline" style="margin:0">The best education, the best environment</p>

  <div class="photo" role="img" aria-label="Photo of a smiling student with earphones holding a book between library shelves"></div>

  <h2 class="centered cta" style="margin:0">Find your answers &amp; more!</h2>

  <p class="centered enquire" style="margin:0">Enquiry us today!</p>
  <p class="centered phone" style="margin:0">+617 3000 4821</p>
  <p class="centered email" style="margin:0">enquiries@harlowinstitute.net.au</p>

  <div class="web-strip">www.harlowinstitute.net.au</div>
</main>
</body>
</html>
```